New Company Business Card Design

I have a new company logo and I want a new business card design. I dont know if the logo file i attached is in the correct format or quality. We are a New York City Specialty construction Firm specializing in high risk out of the box projects. I want a simple and classy business card that people will his card is as crisp as the work his company does.

Target Market(s)

Clients in the heavy construction industry in New York City

Industry/Entity Type

Construction Company

Contact Information for Business Card

Simple Classy - DIFFERENT

Font styles to use
Other font styles liked:
• Mach the logo font in some way

Colors

Designer to choose colors to be used in the design.

Requirements
Must have
• Uniqueness
Nice to have
• Nothing particular - Just different and classy - Timeless
Should not have
• Goofy Shit or Gimmicky shit

```html
<!DOCTYPE html>
<html lang="en">
<head>
<meta charset="utf-8">
<title>Korvath Builders, Inc. – Business Card</title>
<link rel="stylesheet" href="https://fonts.googleapis.com/css2?family=Roboto+Condensed:wght@700&family=Roboto:wght@400;500&display=swap">
<style>
  :root {
    --backdrop: #3b3c3f;
    --card: #1f2022;
    --card-edge: #2a2b2e;
    --brand-blue: #1e78d2;
    --name-blue: #1759bd;
    --text-light: #f2f2f2;
    --text-muted: #d8d8d8;
    --divider: #cfcfcf;
  }
  * { margin: 0; padding: 0; box-sizing: border-box; }
  html, body { width: 1200px; height: 900px; overflow: hidden; }
  body {
    background: var(--backdrop);
    font-family: "Roboto", Arial, sans-serif;
    color: var(--text-light);
    display: flex;
    flex-direction: column;
    align-items: center;
    justify-content: center;
    gap: 34px;
  }
  .card {
    position: relative;
    width: 680px;
    height: 389px;
    background: var(--card);
    border: 1px solid var(--card-edge);
    box-shadow: 0 14px 30px rgba(0,0,0,0.45);
  }

  /* Front */
  .card-front {
    display: flex;
    flex-direction: column;
    align-items: center;
    justify-content: center;
    gap: 40px;
  }
  .brand-name {
    font-family: "Roboto Condensed", "Arial Narrow", sans-serif;
    font-weight: 700;
    font-size: 58px;
    line-height: 1;
    color: var(--brand-blue);
    text-transform: uppercase;
    text-align: center;
    letter-spacing: 1px;
  }
  .front-web {
    font-size: 15px;
    letter-spacing: 8px;
    color: var(--text-muted);
  }

  /* Back */
  .identity {
    position: absolute;
    right: 360px;
    top: 128px;
    text-align: right;
  }
  .person-name {
    font-family: "Roboto Condensed", "Arial Narrow", sans-serif;
    font-weight: 700;
    font-size: 38px;
    line-height: 1;
    color: var(--name-blue);
    text-transform: uppercase;
  }
  .person-title {
    margin-top: 4px;
    font-size: 17px;
    font-weight: 500;
    text-transform: uppercase;
    color: var(--text-light);
  }
  .divider {
    position: absolute;
    left: 342px;
    top: 108px;
    width: 2px;
    height: 140px;
    background: linear-gradient(to bottom, transparent, var(--divider) 25%, var(--divider) 75%, transparent);
  }
  .contact-list {
    position: absolute;
    left: 372px;
    top: 120px;
    list-style: none;
  }
  .contact-item {
    display: flex;
    align-items: center;
    gap: 10px;
    height: 25px;
    font-size: 16px;
    color: var(--text-light);
  }
  .icon {
    width: 16px;
    height: 16px;
    flex: none;
    fill: var(--brand-blue);
  }
  .address {
    position: absolute;
    left: 120px;
    bottom: 62px;
    display: flex;
    align-items: center;
    gap: 6px;
    font-size: 17px;
    color: var(--text-light);
  }
</style>
</head>
<body>

  <section class="card card-front">
    <div class="brand-name">Korvath<br>Builders, Inc.</div>
    <div class="front-web">www.korvathbuild.com</div>
  </section>

  <section class="card card-back">
    <div class="identity">
      <div class="person-name">Daniel Reyes</div>
      <div class="person-title">CEO/Founder</div>
    </div>

    <div class="divider"></div>

    <ul class="contact-list">
      <li class="contact-item">
        <svg class="icon" viewBox="0 0 24 24" aria-hidden="true"><path d="M6.6 10.8a15.2 15.2 0 0 0 6.6 6.6l2.2-2.2a1 1 0 0 1 1-.25 11.4 11.4 0 0 0 3.6.57 1 1 0 0 1 1 1V20a1 1 0 0 1-1 1A17 17 0 0 1 3 4a1 1 0 0 1 1-1h3.5a1 1 0 0 1 1 1c0 1.25.2 2.45.57 3.57a1 1 0 0 1-.25 1z"/></svg>
        555 201 4837
      </li>
      <li class="contact-item">
        <svg class="icon" viewBox="0 0 24 24" aria-hidden="true"><path d="M7 1h10a2 2 0 0 1 2 2v18a2 2 0 0 1-2 2H7a2 2 0 0 1-2-2V3a2 2 0 0 1 2-2zm0 3v14h10V4zm5 15.5a1.2 1.2 0 1 0 0 2.4 1.2 1.2 0 0 0 0-2.4z"/></svg>
        555 318 6624
      </li>
      <li class="contact-item">
        <svg class="icon" viewBox="0 0 24 24" aria-hidden="true"><path d="M6 2h10l2 2v5H6zM3 10h18a2 2 0 0 1 2 2v7h-4v3H5v-3H1v-7a2 2 0 0 1 2-2zm4 6v4h10v-4z"/></svg>
        555 742 0915
      </li>
      <li class="contact-item">
        <svg class="icon" viewBox="0 0 24 24" aria-hidden="true"><path d="M2 5h20v14H2zm2 2v.4l8 5.2 8-5.2V7zm0 2.8V17h16V9.8l-8 5.2z"/></svg>
        info@korvathbuild.com
      </li>
      <li class="contact-item">
        <svg class="icon" viewBox="0 0 24 24" aria-hidden="true"><path d="M12 2a10 10 0 1 0 0 20 10 10 0 0 0 0-20zm6.9 6h-2.9a15 15 0 0 0-1.3-3.6A8 8 0 0 1 18.9 8zM12 4a13 13 0 0 1 1.9 4h-3.8A13 13 0 0 1 12 4zM4.3 14a8 8 0 0 1 0-4h3.4a16 16 0 0 0 0 4zm.8 2h2.9a15 15 0 0 0 1.3 3.6A8 8 0 0 1 5.1 16zM8 8H5.1a8 8 0 0 1 4.2-3.6A15 15 0 0 0 8 8zm4 12a13 13 0 0 1-1.9-4h3.8A13 13 0 0 1 12 20zm2.3-6H9.7a14 14 0 0 1 0-4h4.6a14 14 0 0 1 0 4zm.4 5.6A15 15 0 0 0 16 16h2.9a8 8 0 0 1-4.2 3.6zm1.6-5.6a16 16 0 0 0 0-4h3.4a8 8 0 0 1 0 4z"/></svg>
        www.korvathbuild.com
      </li>
    </ul>

    <div class="address">
      <svg class="icon" viewBox="0 0 24 24" aria-hidden="true"><path d="M12 2a7 7 0 0 0-7 7c0 5.2 7 13 7 13s7-7.8 7-13a7 7 0 0 0-7-7zm0 9.5A2.5 2.5 0 1 1 12 6.5a2.5 2.5 0 0 1 0 5z"/></svg>
      1420 Harbor Street, Brooklyn, New York 11201
    </div>
  </section>

</body>
</html>
```